Business Card Design Project for Investment Fund

Orvanel Asset Partners is an emerging wealth management firm based in New Jersey. It offers superior investment returns to high net worth individuals and institutions by finding undervalued assets.
We recently selected a company logo which was inspired by the Tucana constellation. Beta Tucanae is a group of six stars, containing star cluster 47 Tucanae, rated the second brightest object in the sky.
Now we need a business card design. Since we are an investment firm, the design should project a sense of stability, growth and professionalism. The owner is interested in something simple yet striking, which of course is consistent with the logo.
Target Market(s)
Wealthy individuals, probably middle aged or older, in the US
Industry/Entity Type
Investment

```html
<!DOCTYPE html>
<html lang="en">
<head>
<meta charset="utf-8">
<title>Orvanel Asset Partners – Business Card</title>
<link href="https://fonts.googleapis.com/css2?family=Open+Sans:wght@400;600&display=swap" rel="stylesheet">
<style>
  :root {
    --backdrop: #2b2b2b;
    --card: #ffffff;
    --ink: #2f3a3f;
    --ink-soft: #5f6467;
    --mark-navy: #1f2f8a;
    --rule: #8a8d8f;
  }
  * { margin: 0; padding: 0; box-sizing: border-box; }
  html, body {
    width: 1200px; height: 900px; overflow: hidden;
    background: var(--backdrop);
    font-family: "Open Sans", Arial, sans-serif;
  }
  .stage { position: relative; width: 1200px; height: 900px; }
  .card {
    position: absolute; top: 308px;
    width: 513px; height: 284px;
    background: var(--card);
    border-radius: 18px;
  }
  .card--front { left: 73px; }
  .card--back { left: 616px; }

  .brand-square {
    position: absolute;
    background: var(--mark-navy);
    border-radius: 12%;
  }
  .card--front .brand-square { left: 194px; top: 38px; width: 126px; height: 126px; }
  .card--back .brand-square { left: 84px; top: 70px; width: 88px; height: 88px; }

  .brand-name {
    position: absolute; left: 0; text-align: center;
    color: var(--ink); font-weight: 600; white-space: nowrap;
  }
  .card--front .brand-name { top: 182px; width: 513px; font-size: 31px; letter-spacing: 0.5px; }
  .card--back .brand-name { top: 172px; left: 18px; width: 220px; font-size: 19px; }

  .divider {
    position: absolute; left: 250px; top: 57px;
    width: 1px; height: 178px; background: var(--rule);
  }
  .contact { position: absolute; left: 272px; top: 60px; color: var(--ink-soft); }
  .contact__name { font-size: 21px; line-height: 26px; }
  .contact__title { font-size: 15px; line-height: 20px; margin-bottom: 14px; }
  .contact__line {
    display: flex; align-items: flex-start; gap: 6px;
    font-size: 12.5px; line-height: 16px;
  }
  .contact__line svg { flex: 0 0 11px; width: 11px; height: 11px; margin-top: 3px; fill: var(--ink-soft); }
  .contact__gap { height: 14px; }
</style>
</head>
<body>
<main class="stage">
  <section class="card card--front">
    <div class="brand-square"></div>
    <p class="brand-name">Orvanel Asset Partners</p>
  </section>

  <section class="card card--back">
    <div class="brand-square"></div>
    <p class="brand-name">Orvanel Asset Partners</p>
    <div class="divider"></div>
    <div class="contact">
      <p class="contact__name">Dana Reyes</p>
      <p class="contact__title">CEO</p>
      <div class="contact__line">
        <svg viewBox="0 0 12 12"><path d="M6 0a4 4 0 0 0-4 4c0 3 4 8 4 8s4-5 4-8a4 4 0 0 0-4-4zm0 5.6A1.6 1.6 0 1 1 6 2.4a1.6 1.6 0 0 1 0 3.2z"/></svg>
        <span>48 Harbor Ln.<br>Newark, NJ 07102</span>
      </div>
      <div class="contact__line">
        <svg viewBox="0 0 12 12"><path d="M3 0.5 5 3 3.8 4.3a7 7 0 0 0 3.9 3.9L9 7l2.5 2-1 2C6 11 1 6 1 1.5z"/></svg>
        <span>201-555-0148</span>
      </div>
      <div class="contact__gap"></div>
      <div class="contact__line">
        <svg viewBox="0 0 12 12"><path d="M0 2.5h12v7H0z M0 2.5 6 7l6-4.5" fill="none" stroke="#5f6467" stroke-width="1.2"/></svg>
        <span>dreyes@orvanelassets.com</span>
      </div>
      <div class="contact__line">
        <svg viewBox="0 0 12 12"><g fill="none" stroke="#5f6467" stroke-width="1"><circle cx="6" cy="6" r="5"/><ellipse cx="6" cy="6" rx="2.2" ry="5"/><path d="M1 6h10M2 3.3h8M2 8.7h8"/></g></svg>
        <span>www.orvanelassets.com</span>
      </div>
    </div>
  </section>
</main>
</body>
</html>
```